Flyer for the Harvest Lantern Gathering 2018

Design a flyer for our annual conference with basic information about the conference: conference logo and year,

Location:
Dunmore Community Center (Downtown Portland)
482 Willowby Street, Portland, ME 04117,

Date:
August 24th, 25th and 26th, 2018
Start time 6:00PM

I would like the following three words added to the flyer. These words describe the vision of the conference:
Prophetic, Worship, Prayer

```html
<!DOCTYPE html>
<html lang="en">
<head>
<meta charset="utf-8">
<title>Harvest Lantern Gathering 2018 – Flyer</title>
<link rel="stylesheet" href="https://fonts.googleapis.com/css2?family=Oswald:wght@300;500;600;700&family=Montserrat:wght@400;500;700;900&display=swap">
<style>
  :root {
    --bg-top: #4a0d0a;
    --bg-mid: #2c0806;
    --bg-bottom: #160403;
    --white: #ffffff;
    --gold: #e8c02e;
    --year: #a8841a;
    --orange: #f07a12;
    --ember: #e26a0a;
    --flame-hot: #ffd23a;
    --flame-mid: #f08a16;
    --flame-deep: #a32a0a;
  }
  * { margin: 0; padding: 0; box-sizing: border-box; }
  html, body { width: 900px; height: 1200px; overflow: hidden; background: var(--bg-bottom); }
  .flyer {
    position: relative;
    width: 900px;
    height: 1200px;
    overflow: hidden;
    background:
      radial-gradient(ellipse 70% 45% at 50% 28%, rgba(120, 22, 12, 0.55), transparent 70%),
      linear-gradient(180deg, var(--bg-top) 0%, var(--bg-mid) 45%, var(--bg-bottom) 100%);
    font-family: 'Montserrat', sans-serif;
    color: var(--white);
  }
  .title-art { position: absolute; left: 0; top: 0; width: 900px; height: 620px; }
  .title-art text { font-family: 'Oswald', sans-serif; }
  .title-line { fill: var(--white); font-weight: 600; }
  .title-feature { font-weight: 700; }
  .title-year { fill: var(--year); font-weight: 600; }

  .event-info { position: absolute; left: 0; width: 900px; text-align: center; }
  .event-date { top: 648px; font-size: 31px; letter-spacing: 0.5px; }
  .event-date .month { color: var(--gold); font-weight: 400; margin-right: 14px; }
  .event-date .day { font-weight: 900; }
  .event-time { top: 695px; font-size: 31px; font-weight: 400; }
  .event-time .clock { color: var(--orange); font-weight: 900; }
  .info-rule { position: absolute; left: 414px; top: 754px; width: 70px; height: 2px; background: var(--white); }
  .venue { top: 772px; font-size: 22px; line-height: 32px; }
  .venue .venue-name { color: var(--orange); font-weight: 700; }

  .brand { position: absolute; left: 70px; top: 878px; width: 290px; text-align: center; }
  .brand-mark { display: block; width: 150px; height: 150px; margin: 0 auto; border: 3px solid var(--orange); border-radius: 50%; }
  .brand-name { display: block; margin-top: 22px; font-size: 34px; font-weight: 700; letter-spacing: 3px; color: var(--white); }

  .split-rule { position: absolute; left: 447px; top: 882px; width: 2px; height: 207px; background: linear-gradient(180deg, transparent, var(--ember) 20%, var(--ember) 80%, transparent); }

  .vision { position: absolute; left: 533px; top: 890px; font-family: 'Oswald', sans-serif; font-weight: 600; }
  .vision-word { display: block; font-size: 76px; line-height: 68px; height: 68px; }
  .vision-prophetic { color: var(--orange); font-weight: 500; }
  .vision-prayer { position: relative; color: var(--white); }
  .vision-prayer::before { content: ""; position: absolute; left: 0; top: 2px; width: 367px; height: 66px; background: var(--ember); z-index: -1; }
  .vision-prayer { z-index: 0; }
  .vision-worship { color: var(--white); font-weight: 500; }

  .contact { position: absolute; left: 0; top: 1133px; width: 900px; display: flex; justify-content: center; align-items: center; gap: 14px; font-size: 23px; }
  .contact-icon { width: 24px; height: 24px; }
  .contact-gap { width: 10px; }
</style>
</head>
<body>
<main class="flyer">

  <svg class="title-art" viewBox="0 0 900 620" aria-label="Harvest Lantern Gathering 2018">
    <defs>
      <linearGradient id="flameFill" x1="0" y1="0" x2="0" y2="1">
        <stop offset="0" stop-color="var(--flame-hot)"/>
        <stop offset="0.45" stop-color="var(--flame-mid)"/>
        <stop offset="1" stop-color="var(--flame-deep)"/>
      </linearGradient>
    </defs>
    <text class="title-line" x="96" y="153" font-size="150" textLength="720" lengthAdjust="spacingAndGlyphs">HARVEST</text>
    <text class="title-feature" x="96" y="462" font-size="330" textLength="560" lengthAdjust="spacingAndGlyphs" fill="url(#flameFill)">LANTERN</text>
    <text class="title-year" transform="translate(826 454) rotate(-90)" font-size="196" textLength="283" lengthAdjust="spacingAndGlyphs">2018</text>
    <text class="title-line" x="99" y="607" font-size="170" textLength="712" lengthAdjust="spacingAndGlyphs">GATHERING</text>
  </svg>

  <p class="event-info event-date"><span class="month">AUGUST</span> <span class="day">24TH, 25TH</span> &amp; <span class="day">26TH</span>, 2018</p>
  <p class="event-info event-time">START TIME <span class="clock">6:00PM</span></p>
  <div class="info-rule"></div>
  <p class="event-info venue"><span class="venue-name">Dunmore Community Center</span> (Downtown Portland)<br>482 Willowby Street, Portland, ME 04117,</p>

  <div class="brand">
    <span class="brand-mark"></span>
    <span class="brand-name">LANTERNCON</span>
  </div>

  <div class="split-rule"></div>

  <div class="vision">
    <span class="vision-word vision-prophetic">PROPHETIC</span>
    <span class="vision-word vision-prayer">PRAYER</span>
    <span class="vision-word vision-worship">WORSHIP</span>
  </div>

  <div class="contact">
    <svg class="contact-icon" viewBox="0 0 24 24" aria-hidden="true">
      <circle cx="12" cy="12" r="12" fill="var(--gold)"/>
      <path d="M8.2 6.5l2 .1.8 3-1.3 1c.7 1.5 1.8 2.6 3.2 3.2l1-1.3 3 .8.1 2c-.4.8-1.3 1.2-2.2 1.1-4-.6-7.1-3.7-7.7-7.7-.1-.9.3-1.8 1.1-2.2z" fill="var(--bg-mid)"/>
    </svg>
    <span>+1 207 555 0143</span>
    <span class="contact-gap"></span>
    <svg class="contact-icon" viewBox="0 0 24 24" aria-hidden="true">
      <circle cx="12" cy="12" r="12" fill="var(--gold)"/>
      <circle cx="12" cy="12" r="6.5" fill="none" stroke="var(--bg-mid)" stroke-width="1.6"/>
      <path d="M5.5 12h13M12 5.5c-2.5 3.5-2.5 9.5 0 13M12 5.5c2.5 3.5 2.5 9.5 0 13" fill="none" stroke="var(--bg-mid)" stroke-width="1.4"/>
    </svg>
    <span>WWW.LANTERNHALL.ORG</span>
  </div>

</main>
</body>
</html>
```